Stationary Design For New Dynamic Company

Hi there we require stationary designed for our new company, we have used "Pixel Harbor" recently for our logo and were very impressed with all of the designers that contributed towards the final result.
What we require now is the following:
Letter head layout (A4)
Business Cards (5 people)
With Compliments slips
Envelopes
Email stationary
We would like to use our current logo design and I have included it for your use (JPEG is the one we have chosen and I have attached an EPS file for your use). Our company specializes in architectural cladding and our products are used by architects, builders and private clients, so we wish for the stationary to be suitable and attractive to our clientele.
I thank everyone in advance for your contributions.
Thank you to all that have provided your designs for this project, I apologize for not providing feedback as I have been away. I have looked at everyone's designs and they all look great and I will come back to those designers that I wish to have changes made sometime today.
Once again a big thank you to all involved.
Business

```html
<!DOCTYPE html>
<html lang="en">
<head>
<meta charset="utf-8">
<title>Northwall Stationery</title>
<link href="https://fonts.googleapis.com/css2?family=Roboto:wght@400;700&display=swap" rel="stylesheet">
<style>
  :root{
    --navy:#0b1640;
    --blue:#14408c;
    --sky:#1fa3e0;
    --orange:#f07a1a;
    --red:#e2401c;
    --paper:#ffffff;
    --ink-light:#dfe6f2;
    --bg-center:#f4f4f4;
    --bg-edge:#c9c9c9;
  }
  html,body{margin:0;padding:0;overflow:hidden;}
  body{font-family:"Roboto",Arial,sans-serif;}
  .board{position:relative;width:1200px;height:911px;overflow:hidden;
    background:radial-gradient(ellipse at 60% 40%,var(--bg-center) 0%,var(--bg-edge) 100%);}
  .sheet{position:absolute;background:var(--paper);box-shadow:0 2px 6px rgba(0,0,0,.25);overflow:hidden;}
  .sheet svg.band{position:absolute;left:0;top:0;width:100%;height:100%;}
  .wordmark{position:absolute;font-weight:700;color:var(--blue);letter-spacing:.2px;white-space:nowrap;}
  .wordmark.light{color:var(--paper);}
  .contact-line{position:absolute;font-size:7.5px;color:var(--paper);white-space:nowrap;}

  .letterhead-back{left:140px;top:30px;width:462px;height:595px;}
  .letterhead-back .wordmark{left:18px;top:50px;font-size:19px;}
  .letterhead-back .contact-line{left:16px;top:578px;}

  .letterhead-front{left:91px;top:205px;width:328px;height:372px;}
  .letterhead-front .wordmark{left:18px;top:337px;font-size:15px;}
  .letterhead-front .address{position:absolute;left:145px;top:332px;padding-left:5px;border-left:1px solid var(--paper);
    font-size:7.5px;line-height:9px;color:var(--paper);}
  .letterhead-front .phones{position:absolute;left:233px;top:337px;font-size:7.5px;line-height:9px;color:var(--paper);}

  .envelope-back{left:544px;top:222px;width:491px;height:226px;}
  .envelope-front{left:660px;top:353px;width:462px;height:274px;border-radius:6px 6px 0 0;}
  .envelope-front .label-band{position:absolute;left:0;top:60px;width:100%;height:81px;background:var(--paper);
    border-bottom:2px solid var(--red);}
  .envelope-front .wordmark{left:66px;top:87px;font-size:21px;}
  .envelope-front .contact-line{left:24px;top:164px;}
  .envelope-front .window{position:absolute;left:53px;top:185px;width:228px;height:58px;background:var(--paper);border-radius:10px;}

  .compliments-slip{left:91px;top:665px;width:412px;height:197px;}
  .compliments-slip .watermark-name{position:absolute;left:170px;top:70px;font-size:30px;font-weight:700;color:var(--ink-light);}
  .compliments-slip .note{position:absolute;left:14px;top:135px;font-size:5.5px;color:#777;}
  .compliments-slip .wordmark{left:14px;top:171px;font-size:13px;}
  .compliments-slip .contact-line{left:42px;top:186px;font-size:7px;}

  .card-front{left:538px;top:672px;width:316px;height:190px;}
  .card-front .wordmark{left:50px;top:86px;font-size:31px;}
  .card-back{left:860px;top:672px;width:314px;height:190px;}
  .card-back .square{position:absolute;left:56px;top:70px;width:34px;height:34px;background:var(--blue);}
  .card-back .person{position:absolute;left:170px;top:56px;font-size:12px;color:#1c2030;}
  .card-back .role{position:absolute;left:170px;top:71px;font-size:8.5px;color:#f5c9a0;}
  .card-back .address{position:absolute;left:170px;top:90px;padding-left:6px;border-left:1.5px solid var(--orange);
    font-size:9px;line-height:11px;color:#1c2030;}
  .card-back .phones{position:absolute;left:170px;top:135px;font-size:9px;line-height:11px;color:#1c2030;}
</style>
</head>
<body>
<main class="board">

  <section class="sheet letterhead-back">
    <svg class="band" viewBox="0 0 462 595" preserveAspectRatio="none">
      <defs><linearGradient id="orangeBand" x1="0" x2="1"><stop offset="0" stop-color="var(--red)"/><stop offset=".5" stop-color="var(--orange)"/><stop offset="1" stop-color="var(--red)"/></linearGradient></defs>
      <polygon points="0,569 409,569 462,527 462,595 0,595" fill="url(#orangeBand)"/>
    </svg>
    <div class="wordmark">NORTHWALL</div>
    <div class="contact-line">NORTHWALL | Level 2, 18 Quay Road, CA | +000.555.010 | +000.555.010</div>
  </section>

  <section class="sheet letterhead-front">
    <svg class="band" viewBox="0 0 328 372" preserveAspectRatio="none">
      <defs><linearGradient id="blueBand" x1="0" x2="1"><stop offset="0" stop-color="var(--navy)"/><stop offset=".6" stop-color="var(--sky)"/><stop offset="1" stop-color="var(--blue)"/></linearGradient></defs>
      <polygon points="0,319 262,319 328,292 328,372 0,372" fill="url(#blueBand)"/>
    </svg>
    <div class="wordmark light">NORTHWALL</div>
    <div class="address">NORTHWALL<br>Level 2, 18 Quay Road,<br>CA</div>
    <div class="phones">T +000.555.010<br>F +000.555.010</div>
  </section>

  <section class="sheet envelope-back" style="box-shadow:0 2px 6px rgba(0,0,0,.2);overflow:visible;background:transparent;">
    <svg class="band" viewBox="0 0 491 226" preserveAspectRatio="none" style="overflow:visible">
      <defs><linearGradient id="flap" x1="0" x2="1"><stop offset="0" stop-color="var(--navy)"/><stop offset=".5" stop-color="var(--blue)"/><stop offset="1" stop-color="var(--navy)"/></linearGradient></defs>
      <rect x="0" y="20" width="491" height="206" fill="var(--paper)"/>
      <polyline points="0,226 170,60 330,60 491,226" fill="none" stroke="#e4e4e4" stroke-width="3"/>
      <polygon points="0,0 486,0 501,38 496,47 15,47" fill="url(#flap)"/>
    </svg>
  </section>

  <section class="sheet envelope-front">
    <svg class="band" viewBox="0 0 462 274" preserveAspectRatio="none">
      <defs><linearGradient id="envBody" x1="0" x2="1" y1="0" y2="0"><stop offset="0" stop-color="var(--navy)"/><stop offset=".75" stop-color="var(--blue)"/><stop offset="1" stop-color="var(--navy)"/></linearGradient></defs>
      <rect width="462" height="274" fill="url(#envBody)"/>
    </svg>
    <div class="label-band"></div>
    <div class="wordmark">NORTHWALL</div>
    <div class="contact-line">NORTHWALL | Level 2, 18 Quay Road, CA | +000.555.010 | +000.555.010</div>
    <div class="window"></div>
  </section>

  <section class="sheet compliments-slip">
    <div class="watermark-name">NORTHWALL</div>
    <svg class="band" viewBox="0 0 412 197" preserveAspectRatio="none">
      <defs><linearGradient id="slipBand" x1="0" x2="1"><stop offset="0" stop-color="var(--navy)"/><stop offset="1" stop-color="var(--blue)"/></linearGradient></defs>
      <polygon points="0,140 76,140 128,180 412,180 412,197 0,197" fill="url(#slipBand)"/>
    </svg>
    <div class="note">with compliments</div>
    <div class="wordmark" style="color:var(--orange)">NORTHWALL</div>
    <div class="contact-line">NORTHWALL | Level 2, 18 Quay Road, CA | +000.555.010 | +000.555.010</div>
  </section>

  <section class="sheet card-front">
    <svg class="band" viewBox="0 0 316 190" preserveAspectRatio="none">
      <defs><linearGradient id="cardBand" x1="0" x2="1"><stop offset="0" stop-color="var(--blue)"/><stop offset="1" stop-color="var(--navy)"/></linearGradient></defs>
      <polygon points="0,152 39,179 316,179 316,190 0,190" fill="url(#cardBand)"/>
    </svg>
    <div class="wordmark">NORTHWALL</div>
  </section>

  <section class="sheet card-back">
    <svg class="band" viewBox="0 0 314 190" preserveAspectRatio="none">
      <defs><linearGradient id="cardOrange" x1="0" x2="1"><stop offset="0" stop-color="var(--red)"/><stop offset="1" stop-color="var(--orange)"/></linearGradient></defs>
      <polygon points="0,179 275,179 314,152 314,190 0,190" fill="url(#cardOrange)"/>
    </svg>
    <div class="square"></div>
    <div class="person">DANIEL REEVE</div>
    <div class="role">CEO</div>
    <div class="address">NORTHWALL<br>Level 2, 18 Quay Road,<br>CA</div>
    <div class="phones">T +000.555.010<br>F +000.555.010</div>
  </section>

</main>
</body>
</html>
```